Business / Stationery Design Project

Hi,

I need business cards and all other stationary designed for my new finance broking business.

Stationary required:

Business card
Letter head
with compliments
envelopes

There is gold in the logo design so some gold would be good and open to other creative ideas / colours.

Regards
Milo
Updates

Target Market(s)

Small to medium business customers. Also to appeal to referrers who include accounting firms and other associated professionals (valuers etc)

Industry/Entity Type

Finance

Requirements
Must have
• Professional, classy look.

```html
<!DOCTYPE html>
<html lang="en">
<head>
<meta charset="utf-8">
<title>Harlow Finance — Stationery Set</title>
<link href="https://fonts.googleapis.com/css2?family=Cinzel:wght@500&family=Lora:wght@400&display=swap" rel="stylesheet">
<style>
  :root{
    --backdrop:#e8e3db;
    --paper:#f4f0e8;
    --paper-white:#fbfaf7;
    --espresso:#2f170b;
    --gold:#c7a25c;
    --ink:#2a1a12;
    --cream-text:#f6efe4;
  }
  *{box-sizing:border-box;margin:0;padding:0}
  html,body{width:1200px;height:900px;overflow:hidden}
  body{background:var(--backdrop);position:relative;font-family:"Lora",Georgia,serif;color:var(--ink)}
  .piece{position:absolute;box-shadow:0 2px 6px rgba(0,0,0,.18)}

  .wordmark{display:inline-flex;flex-direction:column;align-items:center;font-family:"Cinzel",Georgia,serif;font-weight:500;line-height:1;text-transform:uppercase}
  .wordmark .name{letter-spacing:.02em}
  .wordmark .sub{letter-spacing:.55em;margin-right:-.55em}
  .wordmark--dark{color:var(--ink)}
  .wordmark--light{color:var(--cream-text)}
  .mark-dot{display:inline-block;border-radius:50%;background:var(--gold)}
  .brand{display:flex;align-items:center;gap:10px}

  /* logo sheet */
  .logo-sheet{left:905px;top:0;width:295px;height:258px;background:#fff;display:flex;align-items:center;justify-content:center;box-shadow:none;z-index:5}
  .logo-sheet .name{font-size:40px}
  .logo-sheet .sub{font-size:12px;margin-top:6px}
  .logo-sheet .mark-dot{width:14px;height:14px}

  /* letterhead */
  .letterhead{left:44px;top:70px;width:483px;height:680px;background:var(--paper)}
  .letterhead .brand-top{position:absolute;left:30px;top:40px}
  .letterhead .brand-top .name{font-size:22px}
  .letterhead .brand-top .sub{font-size:7px;margin-top:3px}
  .letterhead .rule{position:absolute;left:286px;top:28px;width:1px;height:62px;background:var(--gold)}
  .letterhead .address{position:absolute;left:316px;top:26px;width:150px;font-size:6.5px;line-height:11px}
  .letterhead .brand-foot{position:absolute;left:220px;top:640px}
  .letterhead .brand-foot .name{font-size:13px}
  .letterhead .brand-foot .sub{font-size:4.5px;margin-top:2px}

  /* presentation folder */
  .folder{left:352px;top:188px;width:478px;height:684px;background:var(--paper)}
  .folder svg{position:absolute;inset:0}
  .folder .brand{position:absolute;left:0;right:0;top:30px;justify-content:center}
  .folder .name{font-size:18px}
  .folder .sub{font-size:6px;margin-top:2px}

  /* compliments slip */
  .compliments{left:524px;top:292px;width:306px;height:238px;background:var(--espresso)}
  .compliments .brand{position:absolute;left:34px;top:56px}
  .compliments .name{font-size:18px}
  .compliments .sub{font-size:6px;margin-top:2px}
  .compliments .note{position:absolute;left:32px;top:120px;width:120px;font-size:7px;line-height:12.5px;color:var(--cream-text)}

  /* envelope */
  .envelope{left:833px;top:358px;width:367px;height:242px;background:var(--paper-white)}
  .envelope svg{position:absolute;inset:0}
  .envelope .brand{position:absolute;right:38px;top:82px}
  .envelope .name{font-size:18px}
  .envelope .sub{font-size:6px;margin-top:2px}

  /* business cards */
  .card-front{left:845px;top:620px;width:246px;height:110px;border-radius:12px;background:var(--espresso);display:flex;align-items:center;justify-content:center}
  .card-front .name{font-size:15px}
  .card-front .sub{font-size:5px;margin-top:2px}
  .card-upright{left:1116px;top:566px;width:84px;height:224px;border-radius:12px 0 0 12px;background:var(--espresso)}
  .card-upright .brand{position:absolute;left:50%;top:50%;transform:translate(-50%,-50%) rotate(90deg)}
  .card-upright .name{font-size:15px}
  .card-upright .sub{font-size:5px;margin-top:2px}
  .card-back{left:865px;top:780px;width:250px;height:112px;border-radius:12px;background:var(--paper-white)}
  .card-back .brand{position:absolute;left:46px;top:66px}
  .card-back .name{font-size:15px}
  .card-back .sub{font-size:5px;margin-top:2px}
  .card-back .rule{position:absolute;left:130px;top:28px;width:1px;height:64px;background:var(--gold)}
  .card-back .details{position:absolute;left:144px;top:24px;width:100px;font-size:6.5px;line-height:11px}
</style>
</head>
<body>

  <section class="piece letterhead" aria-label="Letterhead">
    <div class="brand brand-top"><span class="wordmark wordmark--dark"><span class="name">Harlow</span><span class="sub">Finance</span></span></div>
    <span class="rule"></span>
    <p class="address">Lorem ipsum dolor sit amet, sed diam nonummy nibh euismod tincidunt ut wisi enim ad minim veniam, quis nostrud exerci tation ullamcorper suscipit lobortis nisl ut aliquip ex ea commodo consequat. Duis autem vel eum iriure hendrerit in</p>
    <div class="brand brand-foot"><span class="wordmark wordmark--dark"><span class="name">Harlow</span><span class="sub">Finance</span></span></div>
  </section>

  <section class="piece folder" aria-label="Presentation folder">
    <svg width="478" height="684" viewBox="0 0 478 684" aria-hidden="true">
      <path fill="var(--espresso)" d="M0,0 H478 C452,8 446,58 422,74 Q410,84 388,84 H90 Q68,84 56,74 C32,58 26,8 0,0 Z"/>
      <path fill="var(--espresso)" d="M0,684 C26,676 32,624 56,608 Q68,598 90,598 H388 Q410,598 422,608 C446,624 452,676 478,684 Z"/>
    </svg>
    <div class="brand"><span class="wordmark wordmark--light"><span class="name">Harlow</span><span class="sub">Finance</span></span></div>
  </section>

  <section class="piece compliments" aria-label="With compliments slip">
    <div class="brand"><span class="wordmark wordmark--light"><span class="name">Harlow</span><span class="sub">Finance</span></span></div>
    <p class="note">Lorem ipsum dolor sit amet, sed diam nonummy nibh euismod tincidunt ut wisi enim ad minim veniam, quis nostrud exerci tation</p>
  </section>

  <section class="piece envelope" aria-label="Envelope">
    <svg width="367" height="242" viewBox="0 0 367 242" aria-hidden="true">
      <path fill="var(--espresso)" d="M0,0 H367 V162 H108 C62,162 40,118 24,60 Q14,16 0,0 Z"/>
    </svg>
    <div class="brand"><span class="wordmark wordmark--light"><span class="name">Harlow</span><span class="sub">Finance</span></span></div>
  </section>

  <section class="piece card-front" aria-label="Business card front">
    <div class="brand"><span class="wordmark wordmark--light"><span class="name">Harlow</span><span class="sub">Finance</span></span></div>
  </section>

  <section class="piece card-upright" aria-label="Business card front, portrait">
    <div class="brand"><span class="wordmark wordmark--light"><span class="name">Harlow</span><span class="sub">Finance</span></span></div>
  </section>

  <section class="piece card-back" aria-label="Business card back">
    <div class="brand"><span class="wordmark wordmark--dark"><span class="name">Harlow</span><span class="sub">Finance</span></span></div>
    <span class="rule"></span>
    <p class="details">Lorem ipsum dolor sit amet, sed diam nonummy nibh euismod tincidunt ut wisi enim ad minim veniam, quis nostrud exerci tation</p>
  </section>

  <section class="piece logo-sheet" aria-label="Logo">
    <div class="brand"><span class="mark-dot"></span><span class="wordmark wordmark--dark"><span class="name">Harlow</span><span class="sub">Finance</span></span></div>
  </section>

</body>
</html>
```